lumbrett-scope virtual tours is looking for a website redisgn that uses our new logo

Using LBS's logo as a basis, please redesign our website. Our web application developer has a stand-in site up at www.lb-scope.net. LBS is a virtual tour company whose main clients are the owners of real estate and rental properties; however, LBS will produce virtual tours for any person, company, or organization for whatever purpose they see fit to use the tour for. This is a dynamic website consisting of three pages. An index/info page, a contact/web form page, a price listing page, a template for a tour page which will have a height/width 75% iframe that showcases one of our tours (www.lb-scope.net) for an example. What is needed: HTML template design for pages that incorporates logo, custom graphic for mail link, FB link, Twitter link, and Virtual Tour link. We would also like a watermarked developed out of our logo pin (.ai of logo pin included). The watermark should also include the capital letters LBS, be in grayscale, translucent and the masked.
Target Market(s)
Home Owners, Real Estate Agents, Property Managers, Event Managers, Business Owners, Park Owners,
Industry/Entity Type
Real Estate
Number of Pages Required
3 page
Requirements
Must have
- New web design that uses our logo (file included). Must have a custom watermark that uses our custom logo pin (file included). Watermark should be gray scale, translucent, and masked. Custom graphics for homepage link (would like something that uses our logo pin), mail link, facebook link, and twitter link.
Nice to have
- I've uploaded a pdf called pano_vs_spherical.pdf which is a scan of a crude drawing I did that illustrates what we'd like for our info page. Basically we'd like to describe the difference between a panoramic image and a spherical image and to do so we'd like to have some graphical drawings that illustrate which each is. We'd like two separate image files that we can include on our info page. Use the uploaded .pdf as a guide. Would also like images 0-9 of custom numerals that match the theme of the page to be used as part of a visitor counter script.
Should not have
- Do not need html code or stylesheets (css). Would rather you concentrate on graphic design of custom graphics, layout, and color scheme. We have competent web applications developers in our small company who can code, we just need you, the graphic artist to work your magic.

```html
<!DOCTYPE html>
<html lang="en">
<head>
<meta charset="utf-8">
<title>lumbrett-scope virtual tours</title>
<link rel="stylesheet" href="https://fonts.googleapis.com/css2?family=Raleway:wght@400;500;600&family=Lato:wght@400;700&display=swap">
<style>
:root{
  --accent:#c4521f;
  --accent-dark:#a83c17;
  --nav-top:#d2662f;
  --nav-bottom:#b8461b;
  --ink:#333333;
  --body:#4a4a4a;
  --band:#f2f2f2;
  --footer:#3a3a3a;
  --footer-text:#d8d8d8;
  --white:#ffffff;
}
*{margin:0;padding:0;box-sizing:border-box}
html,body{width:811px;height:1200px;overflow:hidden;background:var(--white)}
body{position:relative;font-family:"Lato",sans-serif;color:var(--body)}
.abs{position:absolute}
.heading{font-family:"Raleway",sans-serif;font-weight:500;color:var(--accent);text-transform:uppercase;letter-spacing:.2px}

/* header */
.logo{left:50px;top:18px;display:flex;align-items:center;gap:7px}
.logo-dot{width:20px;height:20px;border-radius:50%;background:var(--accent)}
.logo-name{font-family:"Lato",sans-serif;font-weight:700;color:var(--ink);line-height:1}
.logo-name .main{display:block;font-size:18px}
.logo-name .sub{display:block;font-size:7px;text-align:right;margin-top:2px;letter-spacing:.3px}
.search{left:614px;top:28px;width:147px;height:21px;background:#ececec;display:flex;align-items:center;justify-content:space-between;padding:0 8px 0 12px;font-size:8px;font-style:italic;color:#777}

/* nav */
.nav{left:0;top:73px;width:811px;height:33px;background:linear-gradient(var(--nav-top),var(--nav-bottom))}
.nav a{position:absolute;top:0;height:33px;line-height:33px;color:var(--white);font-family:"Raleway",sans-serif;font-size:8.5px;font-weight:500;text-decoration:none;letter-spacing:.3px}
.nav a.active{top:6px;height:21px;line-height:21px;background:var(--accent-dark);padding:0 13px}

/* hero */
.hero{left:50px;top:118px;width:711px;height:324px;background:linear-gradient(100deg,#9a6f86 0%,#c69aab 30%,#e0c1c9 55%,#c9a4b6 80%,#8c6c8c 100%)}
.hero-title{left:32px;top:70px;width:320px;font-family:"Raleway",sans-serif;font-weight:500;font-size:22px;line-height:28px;color:var(--white)}
.hero-text{left:32px;top:142px;width:300px;font-size:10.5px;line-height:19px;color:#2f2a2c}
.btn-light{left:32px;top:213px;width:100px;height:28px;background:var(--white);color:var(--accent);font-family:"Raleway",sans-serif;font-size:8.5px;font-weight:600;display:flex;align-items:center;justify-content:center}
.hero-art{left:350px;top:70px;width:296px;height:204px;border-radius:6px;background:radial-gradient(ellipse at 60% 55%,rgba(255,255,255,.35),rgba(60,50,60,.25) 70%,transparent 100%)}
.dots{display:flex;gap:3px}
.dots span{width:5px;height:5px;border-radius:50%;background:#dadada}
.dots span.on{background:var(--accent)}

/* welcome */
.welcome-title{left:50px;top:497px;font-size:16px}
.portrait{left:50px;top:530px;width:112px;height:123px;background:linear-gradient(160deg,#dfe3e6,#9aa3aa)}
.welcome-text{left:181px;top:528px;width:390px;font-size:8px;line-height:16.2px;text-align:justify}
.btn{height:24px;background:var(--accent);color:var(--white);font-family:"Raleway",sans-serif;font-size:8.5px;font-weight:600;display:flex;align-items:center;justify-content:center}
.services-title{left:598px;top:498px;font-size:16px}
.services-list{left:598px;top:529px;list-style:none}
.services-list li{display:flex;align-items:center;gap:10px;height:23.2px;font-size:8.3px;color:var(--ink)}

/* gallery */
.gallery{left:0;top:690px;width:811px;height:212px;background:var(--band)}
.gallery-title{left:50px;top:31px;font-size:16px}
.thumb{top:60px;width:164px;height:98px;border:2px solid #e2e2e2}

/* pano */
.diagram{top:945px;width:165px;height:109px;border:1px solid #e4e4e4;background:#fafafa}
.diagram-label{top:1066px;width:165px;text-align:center;font-family:"Raleway",sans-serif;font-size:11px;color:var(--ink);letter-spacing:.3px}
.pano-title{left:420px;top:940px;font-size:16px}
.pano-text{left:420px;top:969px;width:338px;font-size:8px;line-height:16.2px;text-align:justify}

/* footer */
.footer{left:0;top:1122px;width:811px;height:78px;background:var(--footer);color:var(--footer-text)}
.footer-links{left:50px;top:22px;font-size:8px;display:flex;gap:7px}
.copyright{left:50px;top:45px;font-size:7.5px}
.follow{left:666px;top:20px;font-size:7.5px}
.social{left:665px;top:39px;display:flex;gap:6px}
.social span{width:19px;height:19px;border-radius:50%}
</style>
</head>
<body>

<header>
  <div class="abs logo">
    <span class="logo-dot"></span>
    <span class="logo-name"><span class="main">lumbrett-scope</span><span class="sub">virtual tours</span></span>
  </div>
  <div class="abs search">Search
    <svg width="9" height="9" viewBox="0 0 10 10"><circle cx="4" cy="4" r="3" fill="none" stroke="#444" stroke-width="1.5"/><line x1="6.2" y1="6.2" x2="9.2" y2="9.2" stroke="#444" stroke-width="1.6"/></svg>
  </div>
</header>

<nav class="abs nav">
  <a class="active" style="left:53px">HOME</a>
  <a style="left:134px">ABOUT US</a>
  <a style="left:219px">SERVICES</a>
  <a style="left:304px">GALLERY</a>
  <a style="left:386px">BLOG</a>
  <a style="left:454px">TESTIMONIALS</a>
  <a style="left:559px">CONTACT US</a>
</nav>

<section class="abs hero">
  <h1 class="abs hero-title">LBS IS A VIRTUAL TOUR COMPANY</h1>
  <p class="abs hero-text">whose main clients are the owners of real estate and rental properties. whose main clients are the owners of real estate and rental properties.</p>
  <div class="abs btn-light">LEARN MORE</div>
  <div class="abs hero-art" role="img" aria-label="Laptop with a magnifying glass and a small house model"></div>
</section>
<div class="abs dots" style="left:388px;top:453px"><span class="on"></span><span></span><span></span><span></span></div>

<section>
  <h2 class="abs heading welcome-title">Welcome to our site</h2>
  <div class="abs portrait" role="img" aria-label="Photo of a smiling businesswoman at a desk"></div>
  <p class="abs welcome-text">If a picture is worth a thousand words then a 360° spherical image is worth 360,000. The world of selling, renting, and leasing your home is a tenuous business, one that can leave many questions unanswered. lumbrett-scope is here to answer those questions. We provide our customers with full-service virtual tours for properties of all types. Our product is one of a kind, offering a service that is not provided by any other area of this industry. Realtors and rental industry members are currently forced to rely on themselves, owners, or property managers to take pictures of the properties.</p>
  <div class="abs btn" style="left:181px;top:632px;width:87px">LEARN MORE</div>

  <h2 class="abs heading services-title">Services</h2>
  <ul class="abs services-list">
    <li><svg width="9" height="9" viewBox="0 0 10 10"><circle cx="5" cy="5" r="4.3" fill="none" stroke="var(--accent)" stroke-width="1.4"/><path d="M3 5h4M5.3 3.2 7 5 5.3 6.8" fill="none" stroke="var(--accent)" stroke-width="1.3"/></svg>Duis aute irure dolor</li>
    <li><svg width="9" height="9" viewBox="0 0 10 10"><circle cx="5" cy="5" r="4.3" fill="none" stroke="var(--accent)" stroke-width="1.4"/><path d="M3 5h4M5.3 3.2 7 5 5.3 6.8" fill="none" stroke="var(--accent)" stroke-width="1.3"/></svg>Reprehenderit in voluptate velit</li>
    <li><svg width="9" height="9" viewBox="0 0 10 10"><circle cx="5" cy="5" r="4.3" fill="none" stroke="var(--accent)" stroke-width="1.4"/><path d="M3 5h4M5.3 3.2 7 5 5.3 6.8" fill="none" stroke="var(--accent)" stroke-width="1.3"/></svg>Sse cillum dolore eu fugiat</li>
    <li><svg width="9" height="9" viewBox="0 0 10 10"><circle cx="5" cy="5" r="4.3" fill="none" stroke="var(--accent)" stroke-width="1.4"/><path d="M3 5h4M5.3 3.2 7 5 5.3 6.8" fill="none" stroke="var(--accent)" stroke-width="1.3"/></svg>Excepteur sint occaecat cupidnon</li>
    <li><svg width="9" height="9" viewBox="0 0 10 10"><circle cx="5" cy="5" r="4.3" fill="none" stroke="var(--accent)" stroke-width="1.4"/><path d="M3 5h4M5.3 3.2 7 5 5.3 6.8" fill="none" stroke="var(--accent)" stroke-width="1.3"/></svg>Proident, sunt in culpa qui</li>
    <li><svg width="9" height="9" viewBox="0 0 10 10"><circle cx="5" cy="5" r="4.3" fill="none" stroke="var(--accent)" stroke-width="1.4"/><path d="M3 5h4M5.3 3.2 7 5 5.3 6.8" fill="none" stroke="var(--accent)" stroke-width="1.3"/></svg>Deserunt mollit anim id est</li>
  </ul>
</section>

<section class="abs gallery">
  <h2 class="abs heading gallery-title">Gallery</h2>
  <div class="abs thumb" style="left:50px;background:linear-gradient(#a9c4dc,#6f7f6a)" role="img" aria-label="Hands holding a tablet in front of a riverside clock tower"></div>
  <div class="abs thumb" style="left:233px;background:linear-gradient(135deg,#1e3f7a,#e8e8e8 60%,#222)" role="img" aria-label="Illustration of a businessman running through a city"></div>
  <div class="abs thumb" style="left:415px;background:linear-gradient(135deg,#0f5fb0,#7fc4ef 60%,#2a7cc8)" role="img" aria-label="Blue digital screens around a globe"></div>
  <div class="abs thumb" style="left:598px;background:linear-gradient(#8c8fa0,#c79a7e 60%,#3a3330)" role="img" aria-label="Crowd at an outdoor festival at dusk"></div>
  <div class="abs dots" style="left:396px;top:178px;gap:6px"><span class="on" style="width:6px;height:6px"></span><span style="width:6px;height:6px"></span></div>
</section>

<section>
  <div class="abs diagram" style="left:50px" role="img" aria-label="Sketch of a spherical image capture"></div>
  <div class="abs diagram-label" style="left:50px">SPHERICAL</div>
  <div class="abs diagram" style="left:234px" role="img" aria-label="Sketch of a panoramic image capture"></div>
  <div class="abs diagram-label" style="left:232px;top:1067px">PANO</div>
  <h2 class="abs heading pano-title">Pano V\S Spherical</h2>
  <p class="abs pano-text">Duis aute irure dolor in reprehenderit in voluptate velit esse cillum dolore eu fugiat nulla pariatur. Excepteur sint occaecat cupidatat non proident, sunt in culpa qui officia deserunt mollit anim id est laborum. Lorem ipsum dolor sit amet, consectetur adipiscing elit, sed do eiusmod tempor incididunt ut labore et dolore magna aliqua.</p>
  <div class="abs btn" style="left:420px;top:1042px;width:87px">LEARN MORE</div>
</section>

<footer class="abs footer">
  <div class="abs footer-links"><span>Home</span><span>|</span><span>About us</span><span>|</span><span>Gallery</span><span>|</span><span>Services</span><span>|</span><span>Contact us</span></div>
  <div class="abs copyright">Copyright © 2015 Yoursite, All rights reserved.</div>
  <div class="abs follow">Follow Us</div>
  <div class="abs social">
    <span style="background:#2d5fa8"></span>
    <span style="background:#3a9ad6"></span>
    <span style="background:#c63a2e"></span>
    <span style="background:#ef8a1c"></span>
  </div>
</footer>

</body>
</html>
```